Ridge 9 Ridge Turbine Rentals Pty Ltd

We are a hire company based on the Gold Coast in Australia, we Hire out Generators to construction sites, music festivals, parties, fetes etc. Anywhere where power is required we can provide it.

Ridge 9 Ridge Turbine Rentals pty Ltd also provides all leads, distribution boards, Qualified Electricians to perform all connections. we offer refuelling services and mechanical services. 24Hr on call service - to an actual english speaking operator.

Slogan ''Power Anywhere Anytime"

Industry/Entity Type

Construction

Contact Information for Business Card

M: 0417285963
E: bookings@ridge9ridgeturbinerentals.com.au

```html
<!DOCTYPE html>
<html lang="en">
<head>
<meta charset="UTF-8">
<title>Ridge 9 Ridge Turbine Rentals – Business Card</title>
<link rel="stylesheet" href="https://fonts.googleapis.com/css2?family=Aclonica&family=Quicksand:wght@400&display=swap">
<style>
  :root {
    --backdrop: #dcdfe1;
    --card: #f1f1f1;
    --ink: #141414;
    --band: #24698a;
    --mark: #3d7fa3;
    --contact: #5a5a5a;
    --icon: #ffffff;
  }
  html, body {
    margin: 0;
    padding: 0;
    width: 1200px;
    height: 800px;
    overflow: hidden;
    background: var(--backdrop);
  }
  .canvas {
    position: relative;
    width: 1200px;
    height: 800px;
    display: flex;
    flex-direction: column;
    align-items: center;
    justify-content: center;
    gap: 40px;
  }
  .card {
    position: relative;
    width: 600px;
    height: 343px;
    background: var(--card);
    border-radius: 6px;
    box-shadow: 0 6px 18px rgba(0,0,0,0.15);
    overflow: hidden;
  }
  .brand {
    position: absolute;
    display: flex;
    align-items: center;
    font-family: "Aclonica", "Arial Black", sans-serif;
    font-weight: 400;
    color: var(--ink);
    text-transform: uppercase;
    white-space: nowrap;
  }
  .brand__square {
    flex: none;
    background: var(--mark);
  }
  .brand__name {
    display: flex;
    flex-direction: column;
    align-items: flex-end;
    line-height: 1.15;
  }
  .brand__title { display: block; }
  .brand__subtitle { display: block; }

  .card--front .brand {
    left: 100px;
    top: 50%;
    transform: translateY(-50%);
    gap: 26px;
  }
  .card--front .brand__square {
    width: 96px;
    height: 96px;
  }
  .card--front .brand__title { font-size: 30px; }
  .card--front .brand__subtitle { font-size: 17px; margin-top: 4px; }

  .card--back .brand {
    left: 20px;
    top: 136px;
    gap: 10px;
  }
  .card--back .brand__square {
    width: 40px;
    height: 40px;
  }
  .card--back .brand__title { font-size: 16px; }
  .card--back .brand__subtitle { font-size: 10px; margin-top: 2px; }

  .band {
    position: absolute;
    inset: 0;
  }
  .contact {
    position: absolute;
    left: 300px;
    font-family: "Quicksand", sans-serif;
    font-size: 12.5px;
    letter-spacing: 0.3px;
    color: var(--contact);
    white-space: nowrap;
  }
  .contact--phone { top: 111px; }
  .contact--email { top: 142px; }
</style>
</head>
<body>
<main class="canvas">
  <section class="card card--front" aria-label="Card front">
    <div class="brand">
      <span class="brand__square"></span>
      <span class="brand__name">
        <span class="brand__title">Ridge 9 Ridge</span>
        <span class="brand__subtitle">Turbine Rentals</span>
      </span>
    </div>
  </section>

  <section class="card card--back" aria-label="Card back">
    <div class="brand">
      <span class="brand__square"></span>
      <span class="brand__name">
        <span class="brand__title">Ridge 9 Ridge</span>
        <span class="brand__subtitle">Turbine Rentals</span>
      </span>
    </div>

    <svg class="band" width="600" height="343" viewBox="0 0 600 343" aria-hidden="true">
      <polyline points="180,-10 276,72 276,190 412,353" fill="none" stroke="var(--band)" stroke-width="20" stroke-linejoin="round"/>
      <path d="M271 112 q-2 0 -2 3 q1 6 7 9 q3 1 3 -1 l-1 -2 l-2 0 q-3 -1 -4 -4 l0 -2 l-1 -3 z" fill="var(--icon)"/>
      <rect x="270" y="143" width="12" height="9" fill="none" stroke="var(--icon)" stroke-width="1.3"/>
      <polyline points="270,143 276,148 282,143" fill="none" stroke="var(--icon)" stroke-width="1.3"/>
    </svg>

    <div class="contact contact--phone">0417285963</div>
    <div class="contact contact--email">bookings@ridge9ridgeturbinerentals.com.au</div>
  </section>
</main>
</body>
</html>
```